Medical Staffing agency

I need a logo design that can stand along and become a brand. I'm not too particular of the design. Want something catchy and hopefully related to the Health field. Not important though. An example of what I'm looking for is the Stride Forge Logo, or the Vantora Logo. Something that can become a brand without having to say the brand name. A bit about my company, I hire medical staff, and contract with other companies to provide anywhere from short term to long term employees. But that is expanding to more than just that.

Industry/Entity Type

Medical

Contact Information for Business Card

Westmere Rehab Services
Dalen Whitcombe, CEO
742 Brookhollow Ave
Suite 48
Clovis, CA 95718

```html
<!DOCTYPE html>
<html lang="en">
<head>
<meta charset="utf-8">
<title>Westmere Rehab Services – Business Card</title>
<link rel="stylesheet" href="https://fonts.googleapis.com/css2?family=Open+Sans:wght@400;600;700&display=swap">
<style>
  :root {
    --backdrop: #e9e6e1;
    --card: #f7f7f7;
    --card-edge: #e2e2e2;
    --brand-blue: #1f6fc1;
    --deep-blue: #1b3f9a;
    --text-grey: #5d6066;
    --swoosh-grey: #8d9096;
    --swoosh-light: #c4c6ca;
  }
  * { box-sizing: border-box; margin: 0; padding: 0; }
  html, body {
    width: 1200px; height: 828px; overflow: hidden;
    background: var(--backdrop);
    font-family: "Open Sans", Arial, sans-serif;
  }
  .canvas {
    position: relative; width: 1200px; height: 828px;
    display: flex; align-items: center; justify-content: center; gap: 60px;
  }
  .card {
    position: relative; width: 510px; height: 292px;
    background: linear-gradient(160deg, #ffffff 0%, var(--card) 70%, #ececec 100%);
    border: 1px solid var(--card-edge);
    box-shadow: 0 10px 24px rgba(0,0,0,0.12);
    overflow: hidden;
  }
  .brand-mark {
    display: flex; align-items: center; gap: 12px;
  }
  .brand-mark .dot {
    width: 34px; height: 34px; border-radius: 50%;
    background: var(--brand-blue); flex: none;
  }
  .brand-mark .name {
    color: var(--brand-blue); font-weight: 600; line-height: 1.1;
  }
  .card-front .brand-mark {
    position: absolute; left: 50%; top: 50%; transform: translate(-50%, -50%);
  }
  .card-front .brand-mark .name { font-size: 24px; }
  .card-back .brand-mark {
    position: absolute; right: 42px; top: 42px;
  }
  .card-back .brand-mark .name { font-size: 20px; }
  .holder {
    position: absolute; left: 40px; top: 118px;
  }
  .holder-name {
    color: var(--deep-blue); font-weight: 700; font-size: 15px; letter-spacing: 0.5px;
    text-transform: uppercase;
  }
  .holder-role { color: var(--text-grey); font-size: 12px; margin-top: 2px; }
  .address { margin-top: 16px; color: var(--text-grey); font-size: 12px; line-height: 1.45; }
  .contacts { list-style: none; margin-top: 14px; color: var(--text-grey); font-size: 11.5px; line-height: 1.6; }
  .contacts li { display: flex; align-items: center; gap: 7px; }
  .contacts svg { width: 11px; height: 11px; flex: none; fill: var(--deep-blue); }
  .swoosh { position: absolute; inset: 0; width: 100%; height: 100%; }
</style>
</head>
<body>
<main class="canvas">
  <section class="card card-front" aria-label="Card front">
    <div class="brand-mark">
      <span class="dot"></span>
      <span class="name">Westmere Rehab<br>Services</span>
    </div>
  </section>

  <section class="card card-back" aria-label="Card back">
    <svg class="swoosh" viewBox="0 0 510 292" aria-hidden="true">
      <defs>
        <linearGradient id="blueBand" x1="0" y1="1" x2="1" y2="0">
          <stop offset="0" stop-color="#1b3f9a"/>
          <stop offset="0.6" stop-color="#2a8ad8"/>
          <stop offset="1" stop-color="#1f6fc1"/>
        </linearGradient>
      </defs>
      <path d="M470 0 C 470 150, 380 250, 250 292 L 290 292 C 420 250, 490 150, 495 0 Z" fill="var(--swoosh-light)"/>
      <path d="M490 0 C 490 160, 410 255, 290 292 L 330 292 C 445 255, 505 160, 510 60 L 510 0 Z" fill="var(--swoosh-grey)"/>
      <path d="M510 70 C 500 180, 430 260, 320 292 L 510 292 Z" fill="url(#blueBand)"/>
    </svg>
    <div class="brand-mark">
      <span class="dot"></span>
      <span class="name">Westmere Rehab<br>Services</span>
    </div>
    <div class="holder">
      <p class="holder-name">Dalen Whitcombe</p>
      <p class="holder-role">CEO</p>
      <p class="address">742 Brookhollow Ave, Suite 48<br>Clovis, CA 95718</p>
      <ul class="contacts">
        <li><svg viewBox="0 0 24 24"><path d="M6.6 10.8a15 15 0 0 0 6.6 6.6l2.2-2.2c.3-.3.7-.4 1-.2 1.1.4 2.3.6 3.6.6.6 0 1 .4 1 1V20c0 .6-.4 1-1 1A17 17 0 0 1 3 4c0-.6.4-1 1-1h3.5c.6 0 1 .4 1 1 0 1.3.2 2.5.6 3.6.1.3 0 .7-.2 1z"/></svg>559 555 0148</li>
        <li><svg viewBox="0 0 24 24"><rect x="2" y="5" width="20" height="14" rx="2"/></svg>dalen@westmererehab.com</li>
        <li><svg viewBox="0 0 24 24"><circle cx="12" cy="12" r="10"/></svg>www.westmererehab.com</li>
      </ul>
    </div>
  </section>
</main>
</body>
</html>
```